Post storm repair flyer

looking for an eye catching 6x9 postcard to send out to single family home owners advertising a "Post Storm Repair Special" explaining that after the recent hurricanes its very important to have your roof checked and any repairs fixed right away before they become a bigger more costly problem and that even though your home wasn't directly hit by the storm the high wind gust could've cause unseen damage.
offer $200 off any repair *some rules may apply
Lark Roofing
888.417.LARK
www.LarkRoofing.example

Roofing

```html
<!DOCTYPE html>
<html lang="en">
<head>
<meta charset="utf-8">
<title>Lark Roofing – Post Storm Repair Special Postcard</title>
<link rel="stylesheet" href="https://fonts.googleapis.com/css2?family=Oswald:wght@400;500;700&family=Montserrat:wght@400;500&display=swap">
<style>
  :root {
    --amber: #f4a812;
    --ink: #000000;
    --paper: #ffffff;
    --slate: #4a4a4c;
    --slate-dark: #3a3a3c;
    --rule: #d9d9d9;
    --stamp: #b4b4b4;
    --backdrop: #7a7a7a;
  }
  html, body {
    margin: 0;
    padding: 0;
    width: 1200px;
    height: 2539px;
    overflow: hidden;
    background: var(--backdrop);
  }
  .postcard {
    position: absolute;
    left: 178px;
    width: 862px;
    height: 575px;
    display: block;
  }
  .postcard--front { top: 1219px; }
  .postcard--back { top: 1879px; }
  .condensed { font-family: "Oswald", "Arial Narrow", sans-serif; }
  .body-copy { font-family: "Montserrat", Arial, sans-serif; }
  .brand-name { font-family: "Montserrat", Arial, sans-serif; font-weight: 500; fill: var(--ink); letter-spacing: 0.5px; }
  .headline-kicker { fill: var(--amber); font-weight: 500; }
  .headline-main { fill: var(--ink); font-weight: 700; }
  .offer-line { fill: var(--amber); font-weight: 500; }
  .offer-amount { fill: var(--ink); }
  .fine-print { fill: var(--ink); font-weight: 500; }
  .band-phone { fill: var(--paper); font-weight: 500; }
  .band-url { fill: var(--ink); font-weight: 500; }
  .section-title { fill: var(--amber); font-weight: 500; }
  .service-item { fill: var(--paper); font-weight: 500; }
  .step-number { fill: var(--amber); font-family: "Montserrat", Arial, sans-serif; font-weight: 500; }
  .step-copy { fill: var(--paper); font-weight: 400; }
</style>
</head>
<body>

<!-- Front side -->
<svg class="postcard postcard--front" viewBox="0 0 862 575" xmlns="http://www.w3.org/2000/svg">
  <defs>
    <linearGradient id="stormSceneTone" x1="0" y1="0" x2="0" y2="1">
      <stop offset="0" stop-color="#a9c6d8"/>
      <stop offset="0.4" stop-color="#6f7d5c"/>
      <stop offset="0.75" stop-color="#4b5a48"/>
      <stop offset="1" stop-color="#b9b4a6"/>
    </linearGradient>
  </defs>
  <rect class="card-surface" x="0" y="0" width="862" height="575" fill="var(--paper)"/>
  <rect class="top-strip" x="0" y="0" width="210" height="14" fill="var(--ink)"/>

  <g role="img" aria-label="Photo of a house with its roof crushed by a fallen tree after a storm">
    <polygon points="292,0 862,0 862,398 570,398" fill="url(#stormSceneTone)"/>
  </g>

  <g class="brand-lockup">
    <rect x="104" y="108" width="16" height="16" fill="var(--ink)"/>
    <text class="brand-name" x="128" y="123" font-size="14">LARK ROOFING</text>
  </g>

  <text class="condensed headline-kicker" x="50" y="191" font-size="58" textLength="268" lengthAdjust="spacingAndGlyphs">Post STORM</text>
  <text class="condensed headline-main" x="48" y="296" font-size="124" textLength="344" lengthAdjust="spacingAndGlyphs">REPAIR</text>
  <text class="condensed headline-main" x="48" y="401" font-size="124" textLength="394" lengthAdjust="spacingAndGlyphs">SPECIAL</text>

  <text class="condensed offer-line" x="50" y="466" font-size="44" textLength="440" lengthAdjust="spacingAndGlyphs">Offer <tspan class="offer-amount">$200</tspan> off any repair</text>
  <text class="condensed fine-print" x="542" y="461" font-size="30" textLength="265" lengthAdjust="spacingAndGlyphs">*some rules may apply</text>

  <polygon class="band-amber" points="0,481 862,481 862,563 0,563" fill="var(--amber)"/>
  <polygon class="band-black" points="0,493 382,493 447,563 0,563" fill="var(--ink)"/>
  <rect class="band-base" x="0" y="563" width="862" height="12" fill="var(--ink)"/>

  <g class="phone-icon" transform="translate(48,518)" fill="var(--paper)">
    <path d="M4 4 C2 10 8 22 18 28 C22 30 26 30 28 27 L29 24 L23 19 L19 22 C15 20 11 15 10 11 L13 7 L9 1 L6 2 Z"/>
  </g>
  <text class="condensed band-phone" x="98" y="549" font-size="40" textLength="204" lengthAdjust="spacingAndGlyphs">888.417.LARK</text>

  <g class="mail-icon" transform="translate(505,514)" fill="none" stroke="var(--ink)" stroke-width="3">
    <rect x="1.5" y="1.5" width="28" height="18" fill="var(--ink)"/>
    <path d="M2 3 L15.5 13 L29 3" stroke="var(--amber)"/>
  </g>
  <text class="condensed band-url" x="555" y="536" font-size="31" textLength="255" lengthAdjust="spacingAndGlyphs">www.LarkRoofing.example</text>
</svg>

<!-- Back side -->
<svg class="postcard postcard--back" viewBox="0 0 862 575" xmlns="http://www.w3.org/2000/svg">
  <defs>
    <linearGradient id="panelTone" x1="0" y1="0" x2="1" y2="1">
      <stop offset="0" stop-color="var(--slate-dark)"/>
      <stop offset="1" stop-color="var(--slate)"/>
    </linearGradient>
    <linearGradient id="shingleTone" x1="0" y1="0" x2="1" y2="1">
      <stop offset="0" stop-color="#8d96a3"/>
      <stop offset="1" stop-color="#4d5562"/>
    </linearGradient>
    <linearGradient id="gableTone" x1="0" y1="0" x2="0" y2="1">
      <stop offset="0" stop-color="#a8c4dc"/>
      <stop offset="1" stop-color="#6c6f6d"/>
    </linearGradient>
  </defs>
  <rect class="card-surface" x="0" y="0" width="862" height="575" fill="var(--paper)"/>
  <rect class="services-panel" x="0" y="0" width="460" height="478" fill="url(#panelTone)"/>

  <g role="img" aria-label="Close-up photo of layered asphalt shingles">
    <polygon points="381,88 412,28 476,28 507,88 476,148 412,148" fill="url(#shingleTone)" stroke="var(--amber)" stroke-width="6"/>
  </g>
  <g role="img" aria-label="Close-up photo of grey roof shingles">
    <polygon points="337,211 368,151 432,151 463,211 432,271 368,271" fill="url(#shingleTone)" stroke="var(--amber)" stroke-width="6"/>
  </g>
  <g role="img" aria-label="Photo of a house gable and roofline against the sky">
    <polygon points="376,336 407,276 471,276 502,336 471,396 407,396" fill="url(#gableTone)" stroke="var(--amber)" stroke-width="6"/>
  </g>

  <text class="condensed section-title" x="48" y="61" font-size="28">Our Services</text>
  <g class="service-list">
    <g transform="translate(64,94)"><circle r="8" fill="var(--amber)"/><path d="M-4 0 L-1 3 L4 -3" fill="none" stroke="var(--paper)" stroke-width="2"/></g>
    <text class="condensed service-item" x="86" y="101" font-size="16">Retail/Commercial Roof Replacement</text>
    <g transform="translate(64,125)"><circle r="8" fill="var(--amber)"/><path d="M-4 0 L-1 3 L4 -3" fill="none" stroke="var(--paper)" stroke-width="2"/></g>
    <text class="condensed service-item" x="84" y="132" font-size="16">Storm Damage Roof Replacement</text>
    <g transform="translate(64,159)"><circle r="8" fill="var(--amber)"/><path d="M-4 0 L-1 3 L4 -3" fill="none" stroke="var(--paper)" stroke-width="2"/></g>
    <text class="condensed service-item" x="84" y="166" font-size="16">New Construction</text>
    <g transform="translate(64,192)"><circle r="8" fill="var(--amber)"/><path d="M-4 0 L-1 3 L4 -3" fill="none" stroke="var(--paper)" stroke-width="2"/></g>
    <text class="condensed service-item" x="84" y="199" font-size="16">Repairs &amp; Restoration</text>
  </g>

  <text class="condensed section-title" x="46" y="251" font-size="28">Lark Roofing Process</text>
  <g class="process-steps body-copy">
    <text class="step-number" x="54" y="302" font-size="22">1.</text>
    <text class="step-copy" x="85" y="292" font-size="12.5">Complementary consultation to</text>
    <text class="step-copy" x="85" y="307" font-size="12.5">access your roofing needs and review</text>
    <text class="step-copy" x="85" y="322" font-size="12.5">our honest recommendations.</text>

    <text class="step-number" x="54" y="363" font-size="22">2.</text>
    <text class="step-copy" x="85" y="353" font-size="12.5">Our team of professionals replace,</text>
    <text class="step-copy" x="85" y="368" font-size="12.5">restore, or repair your roof making the</text>
    <text class="step-copy" x="85" y="383" font-size="12.5">process as stress-free as possible.</text>
    <text class="step-copy" x="85" y="398" font-size="12.5">recommendations.</text>

    <text class="step-number" x="54" y="438" font-size="22">3.</text>
    <text class="step-copy" x="85" y="427" font-size="12.5">100% satisfaction, peace of mind, and</text>
    <text class="step-copy" x="85" y="442" font-size="12.5">continued professional coverage backed</text>
    <text class="step-copy" x="85" y="457" font-size="12.5">by LARK Protection*.</text>
  </g>

  <g class="brand-lockup brand-lockup--small">
    <rect x="566" y="83" width="10" height="10" fill="var(--ink)"/>
    <text class="brand-name" x="582" y="93" font-size="10">LARK ROOFING</text>
  </g>
  <rect class="stamp-box" x="734" y="33" width="80" height="71" fill="var(--stamp)"/>
  <g class="address-lines" stroke="var(--rule)" stroke-width="2">
    <line x1="502" y1="183" x2="815" y2="183"/>
    <line x1="502" y1="228" x2="815" y2="228"/>
    <line x1="502" y1="273" x2="815" y2="273"/>
  </g>

  <polygon class="band-amber" points="0,481 862,481 862,561 0,561" fill="var(--amber)"/>
  <polygon class="band-black" points="0,491 382,491 462,573 0,573" fill="var(--ink)"/>

  <g class="phone-icon" transform="translate(48,518)" fill="var(--paper)">
    <path d="M4 4 C2 10 8 22 18 28 C22 30 26 30 28 27 L29 24 L23 19 L19 22 C15 20 11 15 10 11 L13 7 L9 1 L6 2 Z"/>
  </g>
  <text class="condensed band-phone" x="97" y="551" font-size="40" textLength="204" lengthAdjust="spacingAndGlyphs">888.417.LARK</text>

  <g class="mail-icon" transform="translate(505,512)" fill="none" stroke="var(--ink)" stroke-width="3">
    <rect x="1.5" y="1.5" width="28" height="18" fill="var(--ink)"/>
    <path d="M2 3 L15.5 13 L29 3" stroke="var(--amber)"/>
  </g>
  <text class="condensed band-url" x="555" y="534" font-size="31" textLength="255" lengthAdjust="spacingAndGlyphs">www.LarkRoofing.example</text>
</svg>

</body>
</html>
```